Meridian Forum Flyer

We need a company flyer to present our company. Target group: Senior managers of hospitals / care facilities.
Please use the new text from the document "Kongressflyer.pptx".
Design: The last flyer can be used as a design basis - attached here: "Bright Orbit Flyer High Res Compressed.pdf". Please note the layout of the business card. The flyer must visually match the business card.
Logos for the references attached (KTW, Varmon, Chemnitz, Cologne, Am Lindenhain, Brückwerk, Tobe, PLMR).
Format: DIN A long in portrait format, front and back printed (or open to alternative suggestions if the format does not appear optimal from a design point of view)
Timing: We need the flyer as soon as possible

```html
<!DOCTYPE html>
<html lang="de">
<head>
<meta charset="utf-8">
<title>Meridian Forum Flyer</title>
<link href="https://fonts.googleapis.com/css2?family=Poppins:wght@300;400;500;600;700&display=swap" rel="stylesheet">
<style>
:root{
  --bg:#d9d9d9;
  --paper:#ffffff;
  --ink:#222222;
  --teal:#2f6478;
  --teal-dark:#255668;
  --accent:#e04a4a;
  --logo-slate:#3b5a6b;
  --photo:#6b6b6b;
}
*{margin:0;padding:0;box-sizing:border-box}
html,body{width:1200px;height:1200px;overflow:hidden}
body{background:var(--bg);font-family:'Poppins',sans-serif;color:var(--ink)}
.flyer{position:absolute;left:190px;top:20px;width:820px;height:1160px;background:var(--paper);overflow:hidden}
.abs{position:absolute}
.brand{left:120px;top:82px;font-weight:300;font-size:33px;letter-spacing:5px;color:var(--logo-slate)}
.partner{right:38px;top:72px;display:flex;align-items:center;gap:10px;font-weight:500;font-size:26px;line-height:1;color:var(--logo-slate)}
.partner .sq{width:18px;height:18px;background:var(--logo-slate)}
p,li{font-size:14.2px;line-height:22px}
ul{list-style:none}
li{position:relative;padding-left:25px}
li::before{content:"✓";position:absolute;left:0;top:0;font-size:13px}
li .cont{display:block}
h2{font-weight:600;font-size:17.5px;color:var(--teal);line-height:24px}
.col-l{left:40px;width:380px}
.col-r{left:437px;width:355px}
.rule{left:40px;width:742px;height:2px;background:var(--accent)}
.gap{margin-top:7px}
.refs{left:40px;top:637px;width:760px;height:110px}
.ref{position:absolute;font-weight:600;color:var(--teal);display:flex;align-items:center;gap:8px;font-size:15px;line-height:20px}
.ref .sq{width:12px;height:12px;background:var(--teal);flex:none}
.ref .ci{width:12px;height:12px;border-radius:50%;background:var(--teal);flex:none}
.sub{font-weight:600;font-size:14.2px;line-height:21px}
.pos li{line-height:21px}
.tab{left:0;top:981px;width:374px;height:31px;background:var(--accent);clip-path:polygon(0 0,366px 0,374px 31px,0 31px);color:#fff;font-weight:600;font-size:17px;line-height:31px;padding-left:40px}
.band{left:0;top:1013px;width:820px;height:147px;background:linear-gradient(120deg,var(--teal-dark),var(--teal) 55%,var(--teal-dark))}
.contact{position:absolute;top:19px;display:flex;gap:11px;color:#fff}
.photo{width:81px;height:94px;border-radius:4px;background:linear-gradient(160deg,#8a8a8a,var(--photo))}
.contact .info{font-size:11.5px;line-height:21px;width:135px}
.contact .info b{font-weight:600;font-size:11.5px}
.contact .info .who{line-height:16px;margin-bottom:4px}
</style>
</head>
<body>
<main class="flyer">
  <div class="abs brand">BRIGHT ORBIT</div>
  <div class="abs partner"><span class="sq"></span>Lenzfeld</div>

  <section class="abs col-l" style="top:158px">
    <p>Sie sind Leiter eines Krankenhauses und suchen…</p>
    <ul>
      <li><b>medizinische Fachkräfte</b> für Ihre Klinik oder</li>
      <li><b>herausragende Führungskräfte</b> für Ihre Klinikverwaltung?</li>
    </ul>
    <p class="gap">Möchten Sie dabei auf Augenhöhe begleitet werden? Wir unterstützen Sie gerne.</p>
    <h2 style="margin-top:10px">Wer sind wir?</h2>
    <p style="margin-top:4px">Seit fast 30 Jahren gehört das Unternehmen Lenzfeld</p>
  </section>
  <section class="abs col-r" style="top:158px">
    <p>/ Bright Orbit zu den bedeutensten Personalberatungen im Gesundheitswesen. Die Rekrutierung von Spitzenpersonal für Kliniken ist unsere große Leidenschaft.</p>
    <p class="gap">Durch den Zusammenschluss der beiden Firmen haben wir uns im letzten Jahr modernisiert, digitalisiert und für die Zukunft aufgestellt – ohne dabei die Tradition aus den Augen zu verlieren.</p>
  </section>

  <div class="abs rule" style="top:364px"></div>

  <h2 class="abs" style="left:40px;top:395px">Warum können wir Sie bestmöglich unterstützen?</h2>
  <ul class="abs col-l" style="top:427px">
    <li>Ehrlichkeit ist uns wichtig …<span class="cont">… bei uns bekommen Sie aufrichtiges Marktfeedback und</span><span class="cont">… garantiert keine Versprechungen, die wir nicht halten können</span></li>
    <li>Wir lieben was wir tun …<span class="cont">… und wir arbeiten schnell, effizient und auf Augenhöhe</span></li>
  </ul>
  <ul class="abs col-r" style="top:427px;width:365px">
    <li>Wir sind Spezialisten im Gesundheitswesen …<span class="cont">… unser Team verfügt über fundiertes Marktverständnis</span></li>
    <li>Überragendes Netzwerk …<span class="cont">… in allen Teilsektoren des Gesundheitswesens</span></li>
    <li>Digital …<span class="cont">… unsere Prozesse? Transparent! Unsere Suche für Sie 24/7 einsehbar</span></li>
  </ul>

  <div class="abs rule" style="top:610px"></div>

  <h2 class="abs" style="left:40px;top:637px">Referenzen</h2>
  <div class="abs refs">
    <div class="ref" style="left:0;top:62px"><span class="sq"></span>Tobe</div>
    <div class="ref" style="left:87px;top:42px"><span class="sq"></span>KTW</div>
    <div class="ref" style="left:87px;top:82px"><span class="ci"></span>Varmon</div>
    <div class="ref" style="left:218px;top:22px"><span class="ci"></span><span>Uniklinik<br>Auental</span></div>
    <div class="ref" style="left:218px;top:82px"><span class="sq"></span>Klinikum Selbeck</div>
    <div class="ref" style="left:408px;top:22px"><span class="sq"></span><span>PLMR<br>Nordmark</span></div>
    <div class="ref" style="left:408px;top:82px"><span class="sq"></span>Brückwerk</div>
    <div class="ref" style="left:600px;top:62px"><span class="sq"></span>Am Lindenhain</div>
  </div>

  <div class="abs rule" style="top:769px"></div>

  <h2 class="abs" style="left:40px;top:805px">Was sind typische Positionen, die wir besetzen?</h2>
  <section class="abs col-l pos" style="top:833px">
    <p class="sub">Medizinische Fachkräfte</p>
    <p style="line-height:21px"><b>&gt; 100 Besetzungen</b> in vergangenen 2 Jahren <b>in sämtlichen Fachrichtungen</b>, z.B.</p>
    <ul>
      <li>Chefarzt Gynäkologie / Geburtshilfe</li>
      <li>Chefarzt Radiologie</li>
      <li>Chefarzt Psychiatrie</li>
    </ul>
  </section>
  <section class="abs col-r pos" style="top:833px">
    <p class="sub">Herausragende Führungskräfte</p>
    <p style="line-height:21px"><b>&gt; 150 Besetzungen von Leitungspositionen in sämtlichen Geschäftsbereichen</b> in vergangenen 2 Jahren, z.B.</p>
    <ul>
      <li>Klinik Geschäftsführung / Vorstände</li>
      <li>Leitung Personal</li>
      <li>Leitung Qualitäts- und Risikomanagement</li>
      <li>Leitung Patientenmanagement</li>
    </ul>
  </section>

  <div class="abs tab">Wir freuen uns, von Ihnen zu hören!</div>
  <footer class="abs band">
    <div class="contact" style="left:46px">
      <div class="photo" role="img" aria-label="Porträtfoto der Ansprechpartnerin Büro Hamburg"></div>
      <div class="info"><b>Büro Hamburg</b><div class="who">Dr. med. Lena Hartwig-Solberg</div>lhs@brightorbit.io<br>T +49 172 5550148</div>
    </div>
    <div class="contact" style="left:302px">
      <div class="photo" role="img" aria-label="Porträtfoto der Ansprechpartnerin Büro Wien"></div>
      <div class="info"><b>Büro Wien</b><div class="who">Miriam Eckl</div>me@brightorbit.io<br>T +43 664 5550271</div>
    </div>
    <div class="contact" style="left:557px">
      <div class="photo" role="img" aria-label="Porträtfoto der Ansprechpartnerin Büro Düsseldorf"></div>
      <div class="info"><b>Büro Düsseldorf</b><div class="who">Jana Sophie Wendorf</div>jsw@brightorbit.io<br>T +49 170 5550392</div>
    </div>
  </footer>
</main>
</body>
</html>
```